electric fence manufacturer needs a international catalogue

our company "valmire systems co.,ltd" is base on shenzhen China.
our product is electric fence system. including the energiser and accesories.
our system seperated into 2 section.
1.perimeter security product, pls check attachment for the project picture. we use the high voltage pulse to stop the intruder and bad man. once we touch the wire , you will get shock. but it is safe, just make you unconfortable.
2.farm electric fencing. to keep the animal inside or outside. the same function with security system.
we prefer color such as green. orange.
we want to express is our life is getting peace and comfortable and relax and easy by using electric fencing
3. page size A4

Target Market(s)

global market ,

Industry/Entity Type

Security

```html
<!DOCTYPE html>
<html lang="en">
<head>
<meta charset="utf-8">
<title>VM - 3100SS Solar Energiser — Valmire Systems</title>
<link rel="stylesheet" href="https://fonts.googleapis.com/css2?family=Carlito:wght@400;700&display=swap">
<style>
  :root {
    --leaf: #77ac41;
    --leaf-deep: #6fa23a;
    --ink: #1a1a1a;
    --paper: #ffffff;
    --sun: #fdc800;
    --night: #121212;
    --panel-navy: #2b3f6b;
    --panel-sky: #e9eef3;
  }
  * { box-sizing: border-box; margin: 0; padding: 0; }
  html, body { width: 777px; height: 1200px; overflow: hidden; background: var(--paper); }
  body { position: relative; font-family: "Carlito", "Calibri", sans-serif; color: var(--ink); }

  .tag {
    position: absolute;
    background: var(--leaf);
    color: var(--paper);
    font-size: 39px;
    line-height: 1;
    display: flex;
    align-items: center;
    padding-left: 14px;
  }
  .tag::after {
    content: "";
    position: absolute;
    left: 6%;
    right: 6%;
    bottom: -14px;
    height: 10px;
    background: radial-gradient(ellipse at center, rgba(0,0,0,.28), rgba(0,0,0,0) 70%);
  }
  .tag--wireless { left: 99px; top: 19px; width: 354px; height: 65px; }
  .tag--solar { left: 316px; top: 102px; width: 415px; height: 65px; }

  .product-photo {
    position: absolute;
    left: 24px; top: 178px;
    width: 700px; height: 414px;
    background: linear-gradient(120deg, var(--panel-navy) 0%, #3a5590 45%, var(--panel-sky) 100%);
    border-radius: 4px;
  }

  .model {
    position: absolute;
    left: 49px; top: 590px;
    font-size: 31px;
    font-weight: 700;
    color: var(--leaf-deep);
  }

  .specs { position: absolute; left: 45px; top: 636px; width: 700px; font-size: 23px; line-height: 1.2; }
  .specs h2 { font-size: 24px; font-weight: 700; margin-bottom: 9px; }
  .spec { display: flex; margin-bottom: 11px; }
  .spec__label { white-space: pre; }
  .spec__value { white-space: pre; }
  .spec--wrap .spec__value { width: 500px; white-space: normal; }
  .spec--sub { padding-left: 30px; margin-bottom: 7px; }
  .spec--group { margin-bottom: 10px; }

  .footer { position: absolute; left: 0; top: 1145px; width: 777px; height: 55px; }
  .footer svg { position: absolute; inset: 0; }
  .footer__web { position: absolute; left: 30px; top: 13px; font-size: 23px; color: var(--ink); }
  .footer__tel { position: absolute; left: 442px; top: 12px; font-size: 25px; color: var(--sun); }
  .footer__tel strong { font-weight: 700; margin-left: 4px; }
  .footer__page {
    position: absolute; left: 728px; top: 8px;
    width: 38px; height: 38px; border-radius: 50%;
    background: var(--paper); color: var(--night);
    font-weight: 700; font-size: 21px;
    display: flex; align-items: center; justify-content: center;
  }
</style>
</head>
<body>
  <div class="tag tag--wireless">Wireless Easiness</div>
  <div class="tag tag--solar">Solar (Energy saving)</div>

  <div class="product-photo" role="img" aria-label="Solar panel beside the wall-mounted energiser unit with two wireless remote controls"></div>

  <div class="model">VM - 3100SS</div>

  <section class="specs">
    <h2>Electrical characteristics</h2>
    <div class="spec spec--wrap"><span class="spec__label">Power supply: </span><span class="spec__value">DC 12V(Power by Adapter(AC110-240 V to DC12 V), solar panel(&gt;12V),battery(DC12V))</span></div>
    <div class="spec"><span class="spec__label">Control:  </span><span class="spec__value">Wireless remote control</span></div>
    <div class="spec"><span class="spec__label">Alarm:  </span><span class="spec__value">DC 12V alarm output, connect to siren</span></div>
    <div class="spec"><span class="spec__label">System power consumption:  </span><span class="spec__value">&lt; 10Watt.</span></div>
    <div class="spec"><span class="spec__label">Operating environment Temperature:  </span><span class="spec__value">-40 to +55℃</span></div>
    <div class="spec"><span class="spec__label">Relative humidity: </span><span class="spec__value">&lt; 95%</span></div>
    <div class="spec spec--group"><span class="spec__label">Output parameter:</span></div>
    <div class="spec spec--sub"><span class="spec__label">Output peak voltage:  </span><span class="spec__value">8KV ~ 14KV</span></div>
    <div class="spec spec--sub"><span class="spec__label">Peak current of puise:  </span><span class="spec__value">&lt; 0.1s</span></div>
    <div class="spec spec--sub"><span class="spec__label">Pulse interval time: </span><span class="spec__value">1s</span></div>
    <div class="spec spec--sub"><span class="spec__label">Max energy of pulse: </span><span class="spec__value">1s</span></div>
  </section>

  <footer class="footer">
    <svg width="777" height="55" viewBox="0 0 777 55" aria-hidden="true">
      <rect x="0" y="0" width="777" height="55" fill="var(--sun)"/>
      <polygon points="412,0 777,0 777,55 318,55" fill="var(--night)"/>
    </svg>
    <span class="footer__web">www.valmiresys.com</span>
    <span class="footer__tel">Tel: <strong>86 755 20480316</strong></span>
    <span class="footer__page">3</span>
  </footer>
</body>
</html>
```